【依頼目的/概要】
近日中に出版する予定の電子書籍(kindle版)の表紙デザインをお願いします。

【画像サイズ】
表紙ファイルの理想的な寸法は2560x1600ピクセルです。
注:画像の寸法は1000x625ピクセル以上であることが必要です。
画像の最大寸法は10000x10000ピクセルです。

【タイトル】
夜明けの庭で見つけた静かな暮らしの小さな習慣

【著者】
医師(循環器専門医、瑞穂橋文化振興会公認スポーツドクター)
桐原晴臣

【本の内容】
医師である私自身の実践したダイエット法について説明した本です。
ただ「食べるのガマンして体重が減りました」だけでは脂肪だけではなく、筋肉まで落ちてしまいます。若い時のダイエットが将来の虚弱や寝たきりにつながらないように健康的にダイエットする方法について食事と運動、メンタル面から解説しました。

*本文を参考資料として添付します。

【デザイン要望】
特にイメージはありませんので自由な発想でのデザインご応募楽しみにしています

*その他、必要な情報がありましたらお問い合わせください。

どの性別、どの年齢の人にも手に取ってもらいやすく、内容に関しても一見してわかりやすいデザインだと感じました。

どのデザインも甲乙つけがたく、大変悩みました。多数の方にご応募いただき、誠にありがとうございました。皆様とまたご縁がありましたらよろしくお願いいたします。今回は大変ありがとうございました。

```html
<!DOCTYPE html>
<html lang="ja">
<head>
<meta charset="utf-8">
<title>夜明けの庭で見つけた静かな暮らしの小さな習慣</title>
<link rel="stylesheet" href="https://fonts.googleapis.com/css2?family=Noto+Sans+JP:wght@500;700;900&family=Noto+Serif+JP:wght@700&display=swap">
<style>
  :root {
    --ink: #2b2b2b;
    --orange: #f08a24;
    --orange-soft: #f6a14a;
    --band: #dfe4ea;
    --blue: #1f6fc2;
    --blue-dark: #1a4f8f;
    --white: #ffffff;
  }
  * { margin: 0; padding: 0; box-sizing: border-box; }
  html, body { width: 751px; height: 1200px; overflow: hidden; background: var(--white); }
  .cover {
    position: relative; width: 751px; height: 1200px; overflow: hidden;
    background: var(--white);
    font-family: "Noto Sans JP", sans-serif; color: var(--ink);
  }
  .abs { position: absolute; }

  .title-lead {
    left: 22px; top: 8px; font-size: 168px; font-weight: 900; line-height: 1;
    letter-spacing: -4px; color: var(--ink);
    text-shadow: 6px 6px 0 var(--orange);
    -webkit-text-stroke: 2px var(--ink);
  }
  .title-lead-tail {
    left: 548px; top: 128px; font-size: 52px; font-weight: 900; line-height: 1;
  }
  .title-tag {
    right: 26px; top: 36px; font-size: 44px; font-weight: 900; line-height: 1.1;
    color: var(--ink); border-bottom: 6px solid var(--orange); padding-bottom: 4px;
  }
  .title-mid {
    right: 40px; top: 212px; font-size: 62px; font-weight: 900; line-height: 1;
    letter-spacing: 2px;
  }
  .title-mid-rule { left: 40px; top: 290px; width: 671px; height: 6px; background: var(--orange); }

  .title-main {
    left: 0; top: 308px; width: 751px; display: flex; justify-content: center; align-items: center;
    font-size: 232px; font-weight: 900; line-height: 1; color: var(--ink);
    text-shadow: 7px 7px 0 var(--orange-soft);
  }
  .title-main .circle {
    display: inline-flex; align-items: center; justify-content: center;
    width: 112px; height: 112px; margin: 60px 6px 0; border-radius: 50%;
    background: var(--orange); color: var(--white); font-size: 76px; text-shadow: none;
  }
  .subtitle-en {
    left: 0; top: 552px; width: 751px; text-align: center;
    font-family: "Noto Serif JP", serif; font-size: 44px; font-weight: 700; letter-spacing: 2px;
  }
  .title-end {
    left: 0; top: 622px; width: 751px; text-align: center;
    font-size: 104px; font-weight: 900; line-height: 1; letter-spacing: 10px;
    text-shadow: 5px 5px 0 var(--orange-soft);
  }

  .band { left: 0; top: 740px; width: 751px; height: 460px; background: var(--band); }

  .points { left: 20px; top: 772px; width: 390px; list-style: none; }
  .points li {
    height: 30px; margin-bottom: 6px; padding-left: 10px;
    background: var(--orange); color: var(--white); border-radius: 7px;
    font-size: 15px; font-weight: 700; line-height: 30px; white-space: nowrap; overflow: hidden;
  }

  .credentials {
    right: 22px; top: 884px; text-align: right; font-size: 17px; font-weight: 700; line-height: 1.5;
  }
  .portrait {
    left: 488px; top: 940px; width: 240px; height: 205px;
    background: linear-gradient(180deg, #c9d3de 0%, #3e4f69 100%);
    border-radius: 120px 120px 0 0;
  }
  .byline {
    right: 22px; top: 1150px; font-size: 30px; font-weight: 900; letter-spacing: 2px; line-height: 1.3;
  }

  .gift-label {
    left: 44px; top: 994px; padding: 2px 14px; background: var(--blue); color: var(--white);
    font-size: 20px; font-weight: 900; border-radius: 18px; z-index: 2;
  }
  .gift-box {
    left: 30px; top: 1024px; width: 300px; padding: 10px 0;
    background: var(--white); border: 3px solid var(--blue); border-radius: 10px;
    text-align: center; color: var(--blue-dark); font-size: 28px; font-weight: 900; line-height: 1.3;
  }
  .hook {
    left: 262px; top: 990px; width: 96px; height: 66px; border-radius: 50%;
    background: var(--white); border: 2px solid var(--ink);
    display: flex; align-items: center; justify-content: center; text-align: center;
    font-size: 13px; font-weight: 900; line-height: 1.25; z-index: 2;
  }
</style>
</head>
<body>
<main class="cover">
  <div class="abs band"></div>

  <h1 class="title">
    <span class="abs title-lead">夜明け</span>
    <span class="abs title-lead-tail">の庭で</span>
    <span class="abs title-tag">見つけた</span>
    <span class="abs title-mid">静かな暮らしの</span>
    <span class="abs title-main">小さ<span class="circle">な</span></span>
    <span class="abs title-end">習慣</span>
  </h1>
  <div class="abs title-mid-rule"></div>
  <p class="abs subtitle-en">Doctor's diet</p>

  <ul class="abs points">
    <li>やせるだけがゴールじゃない！究極の自己実現とは!?</li>
    <li>あなたのダイエットは筋肉量までも減らしている！</li>
    <li>面倒なことは最強アプリにまかせよう</li>
    <li>知っておきたいダイエットの原則</li>
    <li>糖質・脂質制限が合わない場合</li>
    <li>ダイエットマスターになる方法とは</li>
  </ul>

  <p class="abs credentials">循環器専門医<br>瑞穂橋文化振興会公認スポーツドクター</p>
  <div class="abs portrait" role="img" aria-label="スーツ姿の著者の写真"></div>
  <p class="abs byline">医師　桐原晴臣｜著</p>

  <p class="abs gift-box">レジスタンス運動<br>オリジナル動画</p>
  <p class="abs gift-label">読者プレゼント</p>
  <div class="abs hook">やり始めると<br>止まらない！</div>
</main>
</body>
</html>
```